Book Cover Design — Literary Memoir — Seven Winters Beneath a Borrowed Moon

I need a professional book cover design for a literary memoir titled Seven Winters Beneath a Borrowed Moon by Dorota K. Whitfield. This project requires two complete cover files — one for the paperback edition and one for the hardcover edition — both built to Printvane print specifications.
The author photograph is attached and is the centerpiece of the front cover. It is not a placeholder. The front cover contains three elements only: the author name, the photograph, and the title. No subtitle, no taglines, no additional elements.
A complete creative brief is attached. Read it in full before submitting a design. It contains all specifications, typography direction, mood references, comparable covers, and file delivery requirements.
A back cover text package is also attached for layout reference. A Canva reference design showing the directional concept is attached — the photograph placement and title position are correct. The typography needs professional resolution.
This is a literary memoir in the tradition of Unlearned, Cartography, and The Paper Orchard. The cover must feel sophisticated, restrained, and literary — not self-help, not inspirational, not decorative.
Two formats required. Paperback and hardcover. Printvane spine templates for both formats are attached.
Full file delivery specifications are in the brief. The color photograph in front of the water in the blue jacket should be used inside the dust jacket with the bio if a dust jacket edition is produced.
Do not use literal interpretations of the title. No whiskey glasses, no alcohol, no angel figurines, no cherubs, no wings, no halos, no religious imagery of any kind. The title is metaphorical. The cover must not illustrate it literally.
The author photograph is the only image on the front cover. Typography, photograph, author name. Nothing else.

BRIEF UPDATE — BACK COVER PHOTOGRAPH AND LAYOUT
Please read before submitting.
A second author photograph is attached to this brief. It is a color photograph and it is specifically for the back cover author bio section only. Do not convert it to black and white. Do not use it on the front cover. The front cover uses only the black and white photograph already provided. The color photograph is for the back cover exclusively. Do not generate, substitute, or alter the image. Use only the file provided.
Back cover layout — exact order top to bottom:
1. Endorsement quotes — top of back cover.
Three endorsement quote placeholders, each approximately two to three lines of quote text followed by the endorser name and credential on the line below. Separate each quote with a thin rule or line. Set in italics, smaller than the jacket copy text. These are placeholders — final quotes are pending.
2. Jacket copy — middle of back cover.
The main descriptive text block. Set in a clean readable serif, slightly larger than the endorsement quotes. Preserve all paragraph breaks exactly as written. Two pull quotes inside the jacket copy must be set in gold, framed by thin gold rules above and below, matching the gold accent color used for BORROWED MOON on the front cover. Use the following final approved text exactly as written:
At forty-three, she stood in a villa in Abu Dhabi at four in the morning and understood that the marriage was over, the career she had given up was not coming back, and the country she was standing in was not hers. She had two boys to raise, a spousal visa, and no plan.
She came by the next move honestly.
A great-grandmother who crossed the Atlantic alone in 1907 and built a life from nothing. A grandmother on the other side, told by an anonymous letter that the blood in her veins was tainted, who answered the letter with the rest of her life. A guardian angel with a slightly crooked halo and a highball in her hand. Four generations of women who refused the smaller life and passed something down that none of them named and none of them had to.
Seven Winters Beneath a Borrowed Moon is the story of what happens when a woman finally stops building someone else's life and starts building her own.
[GOLD PULL QUOTE — framed by thin gold rules above and below, set in gold, centered:]
For anyone who has ever had no choice but to start over — and for anyone still waiting for the courage to.
[End gold pull quote]
Proof that someone has navigated it.
And that you can too.
The closing two lines — Proof that someone has navigated it. and And that you can too. — should each sit on their own line with breathing room around them. They are the closing beats of the back cover.
3. Author bio with photograph — bottom of back cover.
Place the color author photograph on the left side, cropped to approximately a two inch square or whatever proportion fits the layout cleanly. The author bio text runs to the right of the photograph. The author name DOROTA K. WHITFIELD should appear above the bio text in gold caps. Use the following text exactly as written, with one paragraph break inserted between finally behind her. and When the marriage ended:
Dorota K. Whitfield is the founder and CEO of Tallowmere Advisory, an international advisory firm operating across the United States, the Middle East, Africa, and Europe. She gave up a rising career in Pennsylvania state government to support her husband, an KR-19T Osprite pilot, through five combat deployments. She followed him to Abu Dhabi in 2013 believing the hardest years were finally behind her.
When the marriage ended, she was forty-three, in a country that was not hers, with no job and no road back. She rebuilt from nothing and went on to advise governments, ministries, Vantage 400 companies, and members of the Royal Family of Abu Dhabi. She has spoken on stages in over thirty countries. She lives in North Carolina.
4. Barcode and ISBN — lower right corner.
Minimum clear space 2 inches wide by 1.2 inches tall. No other design elements within 0.25 inches of the barcode block.
Background treatment:
The back cover background should not be flat black. Add a subtle texture, very light gradient, or carry a soft element from the front cover photograph into the background to give the back cover visual depth and weight. It should feel finished and intentional, not like an empty void with text dropped onto it.
Typography:
Consistent with the front cover type treatment. Same font family throughout. Endorsement quotes in italics. Jacket copy in roman. Author bio in roman at slightly smaller size than the jacket copy. The gold pull quote inside the jacket copy is set in gold, centered, framed by thin gold rules above and below. The author name above the bio is set in gold caps. All other text is white or very light grey, fully legible against the dark background.
Do not add anything else to the back cover. No additional images, no decorative elements, no additional text beyond what is specified above.

Target Market(s)

Women aged 35 to 65. Readers of literary memoir and narrative nonfiction. Military spouse community. Women navigating reinvention, divorce, or major life transition. Business and leadership audience. Book club readers. Comparable readership to Unlearned by Mira Lockhaven, Cartography by Joss Verhulst, and The Paper Orchard by Corinne Dabney.

Industry/Entity Type

Industry: Book publishing. Literary memoir. Narrative nonfiction.

Font styles to use
Serif
Sans Serif
Other font styles liked:
• Garamond, Caslon, or Freight Display. Clean geometric sans-serif such as Futura or Gotham. Avoid fonts that read as corporate, casual, or decorative. The font chosen for the title must work in both white and gold without losing legibility against the dark photographic background.

Requirements
Must have
• The author photograph — black and white, attached, full bleed, centerpiece of the cover. This is not a placeholder. Do not alter, colorize, or filter it. Author name: DOROTA K. WHITFIELD — top of cover, white, clean and strong. Title: SEVEN WINTERS BENEATH A BORROWED MOON — lower third of cover. BORROWED MOON in gold. All other title words in white. Unified typography — all words of the title must feel like one visual system. This is the primary design challenge. Two complete cover files — one paperback, one hardcover — built to the attached Printvane spine templates. Print-ready PDF both formats, editable source files both formats, front cover flat image for ebook, square audiobook cover 2400 x 2400 pixels.
Nice to have
• A drop cap treatment on the I that opens the title, if the designer can make it feel intentional and unified with the rest of the title rather than decorative. Back cover placeholder showing the design treatment and barcode placement area — full back cover text is provided in the attached back cover package for layout sizing. Subtle gold accent elements if they enhance rather than decorate — the gold should feel intentional, not ornamental.
Should not have
• No subtitle. No tagline. No credential lines. No award badges. No endorsement quotes on the front cover. No brushstroke fonts. No handwritten fonts. No decorative display fonts. No more than two typeface families in the entire design. No additional colors beyond white, gold, and the black and white photograph. No colorizing, filtering, or altering the photograph in any way. No graphic elements, borders, frames, or decorative embellishments. No busy or cluttered layout — negative space is the design language of this cover. Nothing that reads as self-help, inspirational poster, or business book. Do not use literal interpretations of the title. No whiskey glasses, no alcohol, no angel figurines, no cherubs, no wings, no halos, no religious imagery of any kind. The title is metaphorical. The cover must not illustrate it literally. The author photograph is the only image on the front cover. Typography, photograph, author name. Nothing else.

```html
<!DOCTYPE html>
<html lang="en">
<head>
<meta charset="utf-8">
<title>Seven Winters Beneath a Borrowed Moon — Cover Spread</title>
<link rel="stylesheet" href="https://fonts.googleapis.com/css2?family=Playfair+Display:ital,wght@0,400;0,500;1,400&display=swap">
<style>
  :root {
    --page: #ffffff;
    --ink-top: #2c2c2c;
    --ink-mid: #1d1d1d;
    --ink-bottom: #0b0b0b;
    --white: #ffffff;
    --light: #e8e8e8;
    --gold: #f2c318;
    --photo-light: #8a8a8a;
    --photo-mid: #4a4a4a;
  }
  * { margin: 0; padding: 0; box-sizing: border-box; }
  html, body { width: 1200px; height: 1200px; overflow: hidden; background: var(--page); }
  body { position: relative; font-family: "Playfair Display", Georgia, serif; color: var(--white); }

  .spread {
    position: absolute; left: 49px; top: 207px; width: 1109px; height: 791px;
    background: linear-gradient(180deg, var(--ink-top) 0%, #333 45%, var(--ink-mid) 75%, var(--ink-bottom) 100%);
    box-shadow: 0 2px 12px rgba(0,0,0,0.25);
    overflow: hidden;
  }

  /* Back cover */
  .back { position: absolute; left: 31px; top: 34px; width: 468px; }
  .endorsement { margin-bottom: 12px; }
  .endorsement-quote { font-style: italic; font-size: 13.2px; line-height: 17px; color: var(--light); }
  .endorsement-source { font-size: 12.6px; line-height: 17px; color: var(--gold); }
  .jacket-copy {
    margin-top: 14px; font-size: 12.2px; line-height: 16.8px; color: var(--light);
    text-align: justify;
  }
  .bio { margin-top: 22px; font-size: 12.2px; line-height: 16.8px; color: var(--light); text-align: justify; }
  .bio-photo {
    float: left; width: 176px; height: 176px; margin: 2px 11px 4px 0;
    background: linear-gradient(160deg, #9fb0bf 0%, #7d8e9d 45%, #2a3347 75%, #1e2433 100%);
  }
  .bio-name { color: var(--gold); font-weight: 500; }

  /* Spine */
  .spine {
    position: absolute; left: 542px; top: 38px; width: 38px; height: 740px;
    writing-mode: vertical-rl; font-size: 19px; letter-spacing: 0.5px; color: var(--white);
    white-space: nowrap;
  }
  .spine-author { display: inline-block; margin-bottom: 62px; }
  .spine-gold { color: var(--gold); }

  /* Front cover */
  .front-photo {
    position: absolute; left: 700px; top: 0; width: 409px; height: 791px;
    background:
      radial-gradient(ellipse 55% 45% at 78% 58%, var(--photo-light) 0%, var(--photo-mid) 45%, rgba(40,40,40,0) 100%),
      radial-gradient(ellipse 50% 30% at 80% 25%, rgba(170,170,170,0.55) 0%, rgba(40,40,40,0) 100%);
  }
  .front-author {
    position: absolute; left: 600px; top: 34px; width: 500px;
    font-size: 47px; line-height: 1; letter-spacing: 0.5px; color: var(--white);
    text-shadow: 0 2px 6px rgba(0,0,0,0.5);
  }
  .front-title {
    position: absolute; left: 600px; top: 570px; width: 500px;
    text-transform: uppercase; line-height: 1; color: var(--white);
  }
  .title-line { display: block; white-space: nowrap; }
  .title-line--one { font-size: 46px; }
  .drop-cap { font-size: 84px; }
  .title-line--two { font-size: 40px; margin-top: 10px; }
  .title-line--three { font-size: 50px; margin-top: 14px; color: var(--gold); }
</style>
</head>
<body>
  <div class="spread">
    <section class="back">
      <div class="endorsement">
        <p class="endorsement-quote">"Placeholder text for endorsement quote. Final copy pending."</p>
        <p class="endorsement-source">— ENDORSER NAME, TITLE OR AFFILIATION</p>
      </div>
      <div class="endorsement">
        <p class="endorsement-quote">"Placeholder text for endorsement quote. Final copy pending."</p>
        <p class="endorsement-source">— ENDORSER NAME, TITLE OR AFFILIATION</p>
      </div>
      <div class="endorsement">
        <p class="endorsement-quote">"Placeholder text for endorsement quote. Final copy pending."</p>
        <p class="endorsement-source">— ENDORSER NAME, TITLE OR AFFILIATION</p>
      </div>

      <p class="jacket-copy">At forty-three, she stood in a villa in Abu Dhabi at four in the morning and understood that the marriage was over, the career she had given up was not coming back, and the country she was standing in was not hers. She had two boys to raise, a spousal visa, and no plan. She came by the next move honestly. A great-grandmother who crossed the Atlantic alone in 1907 and built a life from nothing. A grandmother on the other side, told by an anonymous letter that the blood in her veins was tainted, who answered the letter with the rest of her life. A guardian angel with a slightly crooked halo and a highball in her hand. Four generations of women who refused the smaller life and passed something down that none of them named and none of them had to. Seven Winters Beneath a Borrowed Moon is the story of what happens when a woman finally stops building someone else's life and starts building her own. For anyone who has ever had no choice but to start over — and for anyone still waiting for the courage to. Proof that someone has navigated it. And that you can too.</p>

      <div class="bio">
        <div class="bio-photo" role="img" aria-label="Colour portrait of the author in a navy jacket in front of water"></div>
        <p><span class="bio-name">Dorota K. Whitfield</span> is the founder and CEO of Tallowmere Advisory, an international advisory firm operating across the United States, the Middle East, Africa, and Europe. She gave up a rising career in Pennsylvania state government to support her husband, an KR-19T Osprite pilot, through five combat deployments. She followed him to Abu Dhabi in 2013 believing the hardest years were finally behind her. When the marriage ended, she was forty-three, in a country that was not hers, with no job and no road back. She rebuilt from nothing and went on to advise governments, ministries, Vantage 400 companies, and members of the Royal Family of Abu Dhabi. She has spoken on stages in over thirty countries. She lives in North Carolina.</p>
      </div>
    </section>

    <div class="spine">
      <span class="spine-author">DOROTA K. WHITFIELD</span><span class="spine-title">SEVEN WINTERS BENEATH A <span class="spine-gold">BORROWED MOON</span></span>
    </div>

    <div class="front-photo" role="img" aria-label="Black and white portrait of the author, half face, against a dark background"></div>
    <h2 class="front-author">DOROTA K. WHITFIELD</h2>
    <h1 class="front-title">
      <span class="title-line title-line--one"><span class="drop-cap">S</span>EVEN WINTERS</span>
      <span class="title-line title-line--two">BENEATH A</span>
      <span class="title-line title-line--three">BORROWED MOON</span>
    </h1>
  </div>
</body>
</html>
```